Wine bottle label design for Coral Ridge Winery

We need a label design for our wine that is being sold in St. John, USVI. We want it to be classic looking, a wine to be taken seriously. Not a whimsical Caribbean design with palm trees and beaches and waves... you get it. The story is about me, my dad and brother making wine for the past 12 years. We're of Italian heritage, so most of the grape varietals will reflect that (No, I don't want any images of Italy on the label :). The price point will be $22-25 retail, so the label should represent that. I have attached what I "threw together" for front/back. I like a simple clean look, black on white background, maybe with another rich accent color (I used hunter green). The back of the label will have a pic of me, my dad and brother. Aside from the "story" and the gov't warning, the design is open for interpretation.
Updates

Project Deadline Extended
Reason: Would like to see more designs different from the sample design I did and posted here.

Target Market(s)

Vistors and locals on the island of St. John who drink wine!

Font styles to use
Serif
Sans Serif

Requirements
Must have
• An upscale, but warm and inviting look and feel. Include logo in label design (Attached).
Nice to have
• It's okay if it's an all front label (See attached sample)
Should not have
• Palm trees, coconuts, waves, pictures grapes, vineyards, or leaves.

```html
<!DOCTYPE html>
<html lang="en">
<head>
<meta charset="UTF-8">
<title>Coral Ridge Winery – Sangiovese Cabernet Label</title>
<link rel="stylesheet" href="https://fonts.googleapis.com/css2?family=Libre+Baskerville:wght@400;700&display=swap">
<style>
  :root {
    --page: #f4f4f3;
    --paper: #ffffff;
    --ink: #1c1c1c;
    --hunter: #3a6b2e;
    --rule: #9a9a9a;
    --edge: #dcdcdc;
  }
  * { margin: 0; padding: 0; box-sizing: border-box; }
  html, body {
    width: 813px;
    height: 1200px;
    overflow: hidden;
    background: var(--page);
  }
  .canvas {
    width: 813px;
    height: 1200px;
    display: flex;
    align-items: center;
    justify-content: center;
  }
  .label {
    position: relative;
    width: 700px;
    height: 640px;
    background: var(--paper);
    border: 1px solid var(--edge);
    box-shadow: 0 6px 24px rgba(0,0,0,0.06);
    font-family: "Libre Baskerville", "Times New Roman", serif;
    color: var(--ink);
    text-align: center;
  }
  .winery-name {
    position: absolute;
    top: 62px;
    left: 0; right: 0;
    font-size: 30px;
    font-weight: 400;
    letter-spacing: 4px;
    line-height: 1.2;
  }
  .winery-sub {
    display: block;
    font-size: 11px;
    letter-spacing: 6px;
    margin-top: 4px;
  }
  .varietal {
    position: absolute;
    top: 222px;
    left: 0; right: 0;
    font-size: 19px;
    color: var(--hunter);
  }
  .divider {
    position: absolute;
    top: 262px;
    left: 130px;
    right: 130px;
    height: 1px;
    background: var(--rule);
  }
  .region {
    position: absolute;
    top: 288px;
    left: 0; right: 0;
    font-size: 44px;
    font-weight: 700;
    letter-spacing: 1px;
  }
  .flourish {
    position: absolute;
    top: 358px;
    left: 50%;
    width: 170px;
    height: 22px;
    margin-left: -85px;
    border-radius: 11px;
    background: linear-gradient(90deg, rgba(58,107,46,0), rgba(58,107,46,0.45) 30%, rgba(58,107,46,0.45) 70%, rgba(58,107,46,0));
  }
  .vintage {
    position: absolute;
    top: 396px;
    left: 0; right: 0;
    font-size: 21px;
    color: var(--hunter);
  }
  .fine-print {
    position: absolute;
    bottom: 44px;
    left: 40px;
    right: 40px;
    display: flex;
    justify-content: space-between;
    align-items: flex-end;
    font-size: 11px;
    line-height: 1.4;
  }
  .fine-print .volume { text-align: left; }
  .fine-print .style { text-align: center; }
  .fine-print .alcohol { text-align: right; }
</style>
</head>
<body>
  <main class="canvas">
    <section class="label">
      <div class="winery-name">CORAL RIDGE<span class="winery-sub">WINERY</span></div>
      <p class="varietal">Sangiovese · Cabernet</p>
      <div class="divider"></div>
      <h1 class="region">ST. JOHN, USVI</h1>
      <div class="flourish" role="img" aria-label="Green ornamental flourish"></div>
      <p class="vintage">2014</p>
      <footer class="fine-print">
        <span class="volume">750 ml</span>
        <span class="style">Red Table Wine</span>
        <span class="alcohol">alc. 13.5%<br>by volume</span>
      </footer>
    </section>
  </main>
</body>
</html>
```